Professional Single Page Website Design for Velloway Advisory

Velloway Advisory is a new business consultancy specializing in providing expert services to small businesses, primarily in the brick-and-mortar retail and food service sectors. We offer a range of services including franchise development and launch, due diligence, and construction management.

Currently, we have a basic website set up at www.vellowayadvisory.example, but we need a professional touch to enhance its design and functionality.

Project Requirements:
- Single Page Design: For now, we need a single page design that effectively showcases who we are, our services, and contact information.
- Future Expansion: The design should be flexible and scalable for future expansion to include additional pages like specific service offerings, about us, and a dedicated contact page.
- Design Aesthetic: We are looking for a modern yet professional design that aligns with our brand identity.
- Logo: We have a logo that we like, which was also sourced from Pixel Forum. The logo files are attached to this project brief.

Key Sections to Include:
- Hero Section: An engaging introduction to Velloway Advisory with a strong visual impact.
- About Us: A brief overview of who we are and our mission.
- Team: Section for the profiles of the two principals.
- Services: A clear and concise presentation of our services, including franchise development, due diligence, and construction management.
- Contact Information: Easy-to-find contact details, including a form for inquiries.
- Call to Action: Encouraging visitors to get in touch with us for consultations or further information.

Design Considerations:
- Ensure the design is responsive and mobile-friendly.
- Include high-quality images and icons that complement our services and industry.
- We do not need development services, this is only a design project.

```html
<!DOCTYPE html>
<html lang="en">
<head>
<meta charset="utf-8">
<title>Velloway Advisory</title>
<link href="https://fonts.googleapis.com/css2?family=Poppins:wght@400;500;600;700;800&display=swap" rel="stylesheet">
<style>
:root{
  --ink:#1d2833;
  --ink-2:#24313d;
  --mint:#8fc8ad;
  --mint-dark:#69b08f;
  --mint-soft:#e7f3ed;
  --text:#2b2f33;
  --muted:#5d6670;
  --white:#ffffff;
  --line:#e2e6e8;
}
*{box-sizing:border-box;margin:0;padding:0}
html,body{width:1200px;height:3706px;overflow:hidden;background:var(--white)}
body{font-family:"Poppins",sans-serif;color:var(--text);position:relative}
.abs{position:absolute}
.ph{position:absolute}
/* hero */
.hero{position:absolute;left:0;top:0;width:1200px;height:610px;overflow:hidden}
.hero-photo{position:absolute;inset:0;background:radial-gradient(ellipse at 70% 45%,#8a6a3e 0%,#3b4a4f 22%,#1c3a45 50%,#142129 100%)}
.hero svg{position:absolute;left:0;top:0}
.nav{position:absolute;top:28px;left:0;width:1200px;height:34px}
.brand{position:absolute;display:flex;align-items:center;gap:10px;font-weight:600;color:var(--white)}
.brand .dot{width:34px;height:34px;border:3px solid var(--mint);border-radius:50%}
.nav .brand{left:147px;top:0;font-size:15px}
.nav-links{position:absolute;left:560px;top:8px;display:flex;gap:26px;font-size:11.5px;color:var(--white)}
.nav-links .on{color:var(--mint);border-bottom:1px solid var(--mint)}
.btn-inq{position:absolute;left:943px;top:2px;width:107px;height:28px;background:var(--mint);color:var(--ink);font-size:11.5px;font-weight:600;display:flex;align-items:center;justify-content:center}
.hero-card{position:absolute;left:182px;top:160px;width:315px;height:331px;background:var(--mint);border-radius:38px;padding:48px 0 0 44px;color:var(--ink)}
.hero-card h1{font-size:39px;font-weight:800;line-height:1.08;letter-spacing:1px}
.hero-card .sub{font-size:28px;font-weight:400;line-height:1.22;margin-top:8px}
.hero-card .small{font-size:11.5px;margin-top:16px}
.hero-card .strong{font-size:13px;font-weight:600;margin-top:2px}
/* intro */
.eyebrow{font-size:10.5px;font-weight:600;color:var(--mint-dark);letter-spacing:.4px}
.section-title{font-size:22px;font-weight:600;color:var(--mint-dark);letter-spacing:.5px}
.intro{left:280px;top:672px;width:640px;text-align:center}
.intro p{font-size:10px;line-height:1.55;color:var(--text);margin-top:6px}
.divider{left:265px;top:803px;width:670px;height:1px;background:var(--line)}
/* about */
.about-mark{left:182px;top:898px;width:283px;height:283px}
.about-text{left:548px;top:880px;width:505px}
.about-text h3{font-size:14px;font-weight:600;color:var(--ink);line-height:1.35;margin:14px 0 12px}
.about-text p{font-size:10px;line-height:1.55;color:var(--text);margin-bottom:12px}
/* services */
.services{left:0;top:1303px;width:689px;height:508px;background:var(--ink)}
.services-photo{left:689px;top:1271px;width:511px;height:540px;border-top-left-radius:60px;background:linear-gradient(150deg,#5a2f72 0%,#3a3550 35%,#7a5a40 70%,#4a3a2c 100%)}
.services .section-title{position:absolute;left:150px;top:78px}
.svc{position:absolute;top:139px;width:126px}
.svc .ic{width:42px;height:42px;border-radius:5px;background:#8a9299;display:flex;align-items:center;justify-content:center}
.svc.on .ic{background:var(--mint)}
.svc .lb{font-size:11.5px;font-weight:500;color:#a9b1b7;margin-top:10px;line-height:1.3;height:30px}
.svc.on .lb{color:var(--mint)}
.svc .ul{height:2px;background:#3a4753;margin-top:8px}
.svc.on .ul{background:var(--mint)}
.services p{position:absolute;left:150px;width:470px;font-size:10px;line-height:1.6;color:#d5dade}
/* team */
.team-title{left:0;top:1870px;width:1200px;text-align:center}
.card{top:1933px;width:432px;height:213px;background:var(--white);border-radius:20px;box-shadow:0 8px 24px rgba(0,0,0,.08)}
.card .photo{position:absolute;left:18px;top:-22px;width:150px;height:150px;border-radius:22px;background:linear-gradient(160deg,#8d8f86,#55616a)}
.card .name{position:absolute;left:190px;top:22px;font-size:14px;font-weight:600;color:var(--ink)}
.card .role{position:absolute;left:190px;top:42px;font-size:11px;color:var(--mint-dark)}
.card .bio{position:absolute;left:190px;top:66px;width:190px;font-size:9.5px;line-height:1.55;color:var(--text)}
.card .icons{position:absolute;left:52px;top:168px;display:flex;gap:10px}
.ci{width:20px;height:20px;border:1px solid #c9cfd3;border-radius:50%;display:flex;align-items:center;justify-content:center}
.ci.on{background:var(--mint);border-color:var(--mint)}
/* cta */
.cta-bg{left:543px;top:2266px;width:657px;height:387px;background:var(--mint-soft)}
.cta-photo{left:0;top:2228px;width:553px;height:425px;border-top-right-radius:120px;background:linear-gradient(180deg,#3e87c9 0%,#8fbde0 45%,#c46a46 70%,#6d7d8c 100%)}
.cta-text{left:614px;top:2370px;width:330px}
.cta-text h2{font-size:22px;font-weight:700;color:var(--ink);line-height:1.2;letter-spacing:.3px}
.cta-text p{font-size:10px;line-height:1.55;margin-top:14px;color:var(--text)}
.btn-dark{background:var(--ink);color:var(--white);font-size:10.5px;font-weight:500;display:flex;align-items:center;justify-content:center}
.cta-text .btn-dark{width:112px;height:28px;margin-top:20px}
/* projects */
.proj-title{left:0;top:2727px;width:1200px;text-align:center}
.proj{border-radius:8px}
.proj-main{left:398px;top:2795px;width:404px;height:348px;background:var(--white);border-radius:10px;box-shadow:0 6px 24px rgba(0,0,0,.15);padding:8px}
.proj-main .ph{left:8px;top:8px;right:8px;bottom:8px;background:linear-gradient(180deg,#6aa0d6 0%,#b9d3e8 40%,#7b8a7a 70%,#3f6b3a 100%)}
.proj-cap{position:absolute;left:8px;bottom:8px;width:165px;height:64px;background:rgba(29,40,51,.85);padding:12px 16px;color:var(--white)}
.proj-cap b{display:block;font-size:10.5px;font-weight:600;color:var(--mint)}
.proj-cap span{font-size:9px;line-height:1.4}
.arrow{left:788px;top:3058px;width:42px;height:42px;border-radius:50%;background:var(--mint);display:flex;align-items:center;justify-content:center}
.view-all{left:565px;top:3190px;width:70px;height:26px}
/* footer */
.footer{left:0;top:3300px;width:1200px;height:406px}
.footer svg{position:absolute;left:0;top:0}
.foot-brand{left:520px;top:3368px;font-size:18px}
.foot-brand .dot{width:44px;height:44px}
.fcol-title{font-size:12px;font-weight:600;color:var(--mint);letter-spacing:.3px}
.fcol{font-size:10.5px;color:var(--white);line-height:1.55}
.frow{display:flex;gap:8px;margin-top:10px;align-items:flex-start}
.qlinks div{margin-top:8px}
.qlinks .on{color:var(--mint);text-decoration:underline}
.map{left:546px;top:3472px;width:158px;height:118px;border-radius:8px;background:linear-gradient(135deg,#eef1ee,#dfe7e2)}
.form{left:757px;top:3383px;width:218px;height:235px;background:var(--mint);border-radius:28px;padding:22px 24px}
.form h4{font-size:12.5px;font-weight:600;color:var(--ink);text-align:center;letter-spacing:.3px}
.field{font-size:9.5px;color:#5f7f70;border-bottom:1px solid #b9dccb;padding:10px 0 8px;margin-top:6px}
.form .btn-dark{width:68px;height:24px;margin:18px auto 0;border-radius:3px}
.copy{left:225px;top:3672px;font-size:10px;color:var(--white)}
.social{left:638px;top:3665px;display:flex;gap:14px}
.social span{width:20px;height:20px;border-radius:50%;background:var(--mint)}
.social span+span{background:none;border:1px solid #5f6d78}
</style>
</head>
<body>

<!-- Hero -->
<section class="hero">
  <div class="hero-photo" role="img" aria-label="Photo of a lit glass office tower model against a dark blurred city"></div>
  <svg width="1200" height="610" viewBox="0 0 1200 610" aria-hidden="true">
    <path d="M0 192 L560 556 Q692 640 820 560 L1200 378 L1200 610 L0 610 Z" fill="#ffffff"/>
    <path d="M530 537 L560 556 Q692 640 820 560 L1200 378" fill="none" stroke="#8fc8ad" stroke-width="6"/>
  </svg>
  <nav class="nav">
    <div class="brand"><span class="dot"></span>Velloway Advisory</div>
    <div class="nav-links"><span class="on">Home</span><span>About Us</span><span>Services</span><span>Team</span><span>Contact Us</span></div>
    <div class="btn-inq">Inquiry Now</div>
  </nav>
  <div class="hero-card">
    <h1>BUILDING<br>SUCCESS</h1>
    <div class="sub">in Southern<br>California</div>
    <div class="small">Expertise at Every Step:</div>
    <div class="strong">From Planning to Execution</div>
  </div>
</section>

<!-- Who we are -->
<section class="abs intro">
  <div class="eyebrow">WHO WE ARE</div>
  <p>At Velloway, we blend innovative strategies with local market expertise to guide your commercial real estate ventures. Whether you're launching a new restaurant, investing in retail spaces, or expanding a franchise, our dedicated team is here to turn your real estate aspirations into tangible success. Dive into a partnership that grows with you.</p>
</section>
<div class="abs divider"></div>

<!-- About -->
<svg class="abs about-mark" viewBox="0 0 283 283" role="img" aria-label="Velloway Advisory mark">
  <rect x="20" y="20" width="243" height="243" rx="56" fill="#8fc8ad"/>
  <text x="141.5" y="150" text-anchor="middle" font-family="Poppins, sans-serif" font-size="26" font-weight="600" fill="#ffffff">Velloway Advisory</text>
</svg>
<section class="abs about-text">
  <div class="section-title">ABOUT US</div>
  <h3>Welcome to Velloway Advisory, your trusted partner in navigating the complexities of the real estate and small business markets.</h3>
  <p>Founded by industry veterans Tomas Varela and Daniel Rhee, we specialize in providing comprehensive services tailored to the unique needs of our clients. Whether you're a franchisee, a new restaurant owner, or a commercial real estate investor, our expertise in due diligence, construction management, and investment property evaluation ensures you make informed, strategic decisions.</p>
  <p>At Velloway Advisory, we are committed to your success. Our approach combines meticulous analysis, strategic insights, and personalized service to help you achieve your business goals. We pride ourselves on our ability to deliver results that exceed expectations, fostering long-term relationships built on trust and excellence.</p>
  <p>Discover how Velloway Advisory can support your business journey. Partner with us and experience the difference our dedication and expertise can make.</p>
</section>

<!-- Services -->
<div class="abs services-photo" role="img" aria-label="Photo of a hand stacking wooden blocks printed with shop fronts"></div>
<section class="abs services">
  <div class="section-title">OUR SERVICES</div>
  <div class="svc on" style="left:150px">
    <div class="ic"><svg width="24" height="24" viewBox="0 0 24 24" fill="none" stroke="#1d2833" stroke-width="1.6"><rect x="3" y="3" width="7" height="7"/><rect x="14" y="3" width="7" height="7"/><rect x="3" y="14" width="7" height="7"/><rect x="14" y="14" width="7" height="7"/></svg></div>
    <div class="lb">Including franchise development</div><div class="ul"></div>
  </div>
  <div class="svc" style="left:313px">
    <div class="ic"><svg width="24" height="24" viewBox="0 0 24 24" fill="none" stroke="#1d2833" stroke-width="1.6"><circle cx="12" cy="12" r="6"/><circle cx="12" cy="12" r="2"/></svg></div>
    <div class="lb">Due diligence</div><div class="ul"></div>
  </div>
  <div class="svc" style="left:476px">
    <div class="ic"><svg width="24" height="24" viewBox="0 0 24 24" fill="none" stroke="#1d2833" stroke-width="1.6"><rect x="5" y="4" width="14" height="17"/><path d="M9 8h6M9 12h6M9 16h6"/></svg></div>
    <div class="lb">Construction management</div><div class="ul"></div>
  </div>
  <p style="top:276px">At Velloway Advisory, our Franchise Development &amp; Launch service is designed to transform your successful business into a thriving franchise. We start by thoroughly evaluating your business model to determine its franchisability. Once confirmed, our team handles every aspect of the franchise setup, including legal documentation, branding, marketing strategies, operational guidelines, and franchisee recruitment.</p>
  <p style="top:380px">Our goal is to ensure a seamless and efficient transition from a single successful location to a robust franchise network, empowering your business to scale effectively and achieve exponential growth. Partner with us to turn your business into a nationwide brand.</p>
</section>

<!-- Team -->
<div class="abs section-title team-title">OUR TEAM</div>
<article class="abs card" style="left:156px">
  <div class="photo" role="img" aria-label="Portrait photo of principal Daniel Rhee"></div>
  <div class="name">Daniel Rhee</div>
  <div class="role">Principal</div>
  <div class="bio">Daniel Rhee is a seasoned real estate expert with extensive experience in project and construction management, and a licensed real estate agent in California. Fluent in both English and Korean,...</div>
  <div class="icons">
    <span class="ci"><svg width="10" height="10" viewBox="0 0 24 24" fill="#1d2833"><path d="M6 2l4 4-2 3a12 12 0 007 7l3-2 4 4-3 4C10 22 2 14 2 5z"/></svg></span>
    <span class="ci"><svg width="10" height="10" viewBox="0 0 24 24" fill="#1d2833"><path d="M2 5h20v14H2z"/></svg></span>
    <span class="ci"><svg width="10" height="10" viewBox="0 0 24 24" fill="none" stroke="#1d2833" stroke-width="3"><path d="M4 12h15M13 6l6 6-6 6"/></svg></span>
  </div>
</article>
<article class="abs card" style="left:612px">
  <div class="photo" role="img" aria-label="Portrait photo of principal Tomas Varela"></div>
  <div class="name">Tomas Varela</div>
  <div class="role">Principal</div>
  <div class="bio">Tomas Varela brings almost 20 years of rich experience as a real estate investor and a pivotal role at one of southern California's largest real estate management firms, where he...</div>
  <div class="icons">
    <span class="ci"><svg width="10" height="10" viewBox="0 0 24 24" fill="#1d2833"><path d="M6 2l4 4-2 3a12 12 0 007 7l3-2 4 4-3 4C10 22 2 14 2 5z"/></svg></span>
    <span class="ci"><svg width="10" height="10" viewBox="0 0 24 24" fill="#1d2833"><path d="M2 5h20v14H2z"/></svg></span>
    <span class="ci on"><svg width="10" height="10" viewBox="0 0 24 24" fill="none" stroke="#ffffff" stroke-width="3"><path d="M4 12h15M13 6l6 6-6 6"/></svg></span>
  </div>
</article>

<!-- Call to action -->
<div class="abs cta-bg"></div>
<div class="abs cta-photo" role="img" aria-label="Photo of modern glass office towers under a blue sky"></div>
<section class="abs cta-text">
  <h2>UNLOCK YOUR BUSINESS POTENTIAL TODAY!</h2>
  <p>At Velloway Advisory, we're dedicated to turning your business aspirations into reality. Our expertise and commitment ensure you make informed, strategic decisions that drive success. Take the first step towards achieving your goals with confidence.</p>
  <div class="btn-dark">Get Started Now</div>
</section>

<!-- Projects -->
<div class="abs section-title proj-title">OUR PROJECT</div>
<div class="abs proj" style="left:0;top:2831px;width:54px;height:278px;border-radius:0 8px 8px 0;background:linear-gradient(180deg,#8aa9c4,#7a5a45)" role="img" aria-label="Photo of a modern house"></div>
<div class="abs proj" style="left:67px;top:2831px;width:276px;height:278px;background:linear-gradient(180deg,#6f9fd0 0%,#dfe6ea 50%,#7c8d84 100%)" role="img" aria-label="Photo of a white modern villa"></div>
<div class="abs proj-main">
  <div class="ph" role="img" aria-label="Photo of a two-storey family house with a garden"></div>
  <div class="proj-cap"><b>LOREM IPSUM</b><span>is simply dummy text of the printing industry.</span></div>
</div>
<div class="abs proj" style="left:858px;top:2831px;width:273px;height:278px;background:linear-gradient(180deg,#3c4e66 0%,#a57a4e 55%,#2e4a5c 100%)" role="img" aria-label="Photo of a modern house at dusk with a pool"></div>
<div class="abs proj" style="left:1145px;top:2831px;width:55px;height:278px;border-radius:8px 0 0 8px;background:linear-gradient(180deg,#7fb0d8,#4d6b4a)" role="img" aria-label="Photo of a house"></div>
<div class="abs arrow"><svg width="20" height="12" viewBox="0 0 20 12" fill="none" stroke="#1d2833" stroke-width="1.8"><path d="M1 6h18M5 2L1 6l4 4M15 2l4 4-4 4"/></svg></div>
<div class="abs btn-dark view-all">View All</div>

<!-- Footer -->
<footer class="abs footer">
  <svg width="1200" height="406" viewBox="0 0 1200 406" aria-hidden="true">
    <path d="M0 200 L440 20 Q600 -30 760 20 L1200 200 L1200 406 L0 406 Z" fill="#1d2833"/>
    <path d="M0 200 L440 20 Q600 -30 760 20 L1200 200" fill="none" stroke="#8fc8ad" stroke-width="6"/>
  </svg>
</footer>
<div class="abs brand foot-brand"><span class="dot"></span>Velloway Advisory</div>
<div class="abs" style="left:225px;top:3468px;width:190px">
  <div class="fcol-title">CONTACT US</div>
  <div class="fcol" style="margin-top:18px">
    <div class="frow"><svg width="11" height="11" viewBox="0 0 24 24" fill="#ffffff"><path d="M6 2l4 4-2 3a12 12 0 007 7l3-2 4 4-3 4C10 22 2 14 2 5z"/></svg>555 010 2468</div>
    <div class="frow"><svg width="11" height="11" viewBox="0 0 24 24" fill="#ffffff"><path d="M2 5h20v14H2z"/></svg>info@vellowayadvisory.example</div>
    <div class="frow"><svg width="11" height="13" viewBox="0 0 24 28" fill="#ffffff"><path d="M12 0a9 9 0 00-9 9c0 7 9 18 9 18s9-11 9-18a9 9 0 00-9-9zm0 12a3 3 0 110-6 3 3 0 010 6z"/></svg><span>Suite 100<br>48 Harbor Lane, Westfield<br>Park</span></div>
  </div>
</div>
<div class="abs" style="left:430px;top:3468px">
  <div class="fcol-title">QUICK LINK</div>
  <div class="fcol qlinks" style="margin-top:10px"><div class="on">Home</div><div>About Us</div><div>Services</div><div>Team</div><div>Contact Us</div></div>
</div>
<div class="abs map" role="img" aria-label="Street map showing the office location"></div>
<section class="abs form">
  <h4>QUICK INQUIRY</h4>
  <div class="field">Name</div>
  <div class="field">Email</div>
  <div class="field">Phone</div>
  <div class="field">Comments</div>
  <div class="btn-dark">Submit</div>
</section>
<div class="abs copy">© 2024 Velloway Advisory. all right reserved</div>
<div class="abs social"><span></span><span></span><span></span></div>

</body>
</html>
```